Family business needs stationery redesign with new logo

Family owned company, established in 1987 wanting a brand 'refresh'. We are an electrical, refrigeration and construction company based in the Barkly Region Northern Territory, Australia. We have a new logo we would like to use which is uploaded along with our current letterhead and email signature. We are also dropping the word 'contractors' so please do not include this on any designs. Please note also, the 'orange' color used in our logo and designs should be Northern Territory red ochre which is as follows:

RGB (Hex): #C75B12
PantoneĀ® 159 C
CMYK: 1 / 74 / 100 / 7

We are needing our stationery redesigned using our new logo. Please include letterheads, business cards, envelopes, and email signatures.

We currently use our business letterheads for quotations, invoices, letters, HR matters, and internal memos.

We also need a separate simplified letterhead for internal paperwork such as employee leave forms, meeting agendas, and meeting minutes etc.
Updates

Reason: Needing more submissions of full package designs. We are wanting all our stationery, including business cards, letterheads, email signatures, envelopes, etc to be cohesive. We also require ALL the information, as supplied on our template letterhead, to be included on the new letterhead designs. including electrical license no.etc Thank you, K&M

Reason: needing more time as work has got in the way of looking over designs. A lot of designs not meeting the brief/criteria.

Industry/Entity Type

Business

Colors
0355a3
f37122

Requirements
Must have
• The 'orange' color used in the designs should be Northern Territory red ochre which is as follows:
• RGB (Hex): #C75B12
• PantoneĀ® 159 C
• CMYK: 1 / 74 / 100 / 7
• ***MUST INCLUDE ALL INFORMATION THAT IS ON OUR CURRENT LETTERHEAD***
Should not have
• Please do not include the word 'contractors'

```html
<!DOCTYPE html>
<html lang="en">
<head>
<meta charset="utf-8">
<title>K&amp;M Business Cards</title>
<link href="https://fonts.googleapis.com/css2?family=Arimo:wght@400;700&display=swap" rel="stylesheet">
<style>
  :root {
    --backdrop: #3a332f;
    --card: #161719;
    --card-edge: #202124;
    --ink-light: #e9e9e9;
    --ink-muted: #8a8b8e;
    --brand-blue: #2b4a9a;
    --brand-ochre: #C75B12;
    --rule: #d9d9d9;
  }
  * { margin: 0; padding: 0; box-sizing: border-box; }
  html, body { width: 1200px; height: 864px; overflow: hidden; }
  body {
    background: var(--backdrop);
    font-family: "Arimo", Arial, sans-serif;
    position: relative;
  }
  .card {
    position: absolute;
    width: 530px;
    height: 303px;
    background: var(--card);
    border: 1px solid var(--card-edge);
    box-shadow: 0 10px 24px rgba(0,0,0,0.45);
  }
  .card--front { left: 45px; top: 150px; }
  .card--back { left: 625px; top: 330px; }

  .front-name {
    position: absolute;
    left: 0; right: 0; top: 112px;
    text-align: center;
    font-size: 34px;
    font-weight: 400;
    color: var(--ink-muted);
    letter-spacing: 4px;
  }
  .front-web {
    position: absolute;
    left: 0; right: 0; top: 196px;
    text-align: center;
    font-size: 13px;
    letter-spacing: 3px;
    color: var(--ink-muted);
  }

  .back-name {
    position: absolute;
    right: 40px; top: 62px;
    font-size: 30px;
    font-weight: 400;
    color: var(--ink-light);
    letter-spacing: 4px;
  }

  .person { position: absolute; left: 34px; top: 62px; }
  .person__name { font-size: 19px; color: var(--brand-blue); }
  .person__role { font-size: 15px; color: var(--brand-ochre); margin-top: 3px; }

  .rule-main {
    position: absolute; left: 34px; right: 34px; top: 118px;
    height: 1px; background: var(--rule);
  }

  .contacts {
    position: absolute; left: 34px; top: 128px;
    list-style: none;
  }
  .contacts li {
    display: flex; align-items: center; gap: 12px;
    font-size: 14px; color: var(--ink-light);
    height: 22px;
  }
  .contacts svg { width: 13px; height: 13px; fill: var(--brand-blue); }

  .rule-address {
    position: absolute; left: 330px; right: 34px; top: 214px;
    height: 1px; background: var(--rule);
  }
  .address {
    position: absolute; right: 34px; top: 224px;
    text-align: right;
    font-size: 14px; line-height: 21px;
    color: var(--ink-light);
  }
  .address__web { letter-spacing: 3px; }
</style>
</head>
<body>
  <section class="card card--front">
    <div class="front-name">K&amp;M</div>
    <div class="front-web">www.kmbuild.com</div>
  </section>

  <section class="card card--back">
    <div class="back-name">K&amp;M</div>

    <div class="person">
      <div class="person__name">Sam Hollis</div>
      <div class="person__role">President</div>
    </div>

    <div class="rule-main"></div>

    <ul class="contacts">
      <li>
        <svg viewBox="0 0 24 24" aria-hidden="true"><path d="M6.6 10.8a15.1 15.1 0 0 0 6.6 6.6l2.2-2.2a1 1 0 0 1 1-.25 11.4 11.4 0 0 0 3.6.57 1 1 0 0 1 1 1V20a1 1 0 0 1-1 1A17 17 0 0 1 3 4a1 1 0 0 1 1-1h3.5a1 1 0 0 1 1 1c0 1.250.2 2.450.57 3.57a1 1 0 0 1-.25 1z"/></svg>
        555 0142 7781
      </li>
      <li>
        <svg viewBox="0 0 24 24" aria-hidden="true"><path d="M7 1h10a2 2 0 0 1 2 2v18a2 2 0 0 1-2 2H7a2 2 0 0 1-2-2V3a2 2 0 0 1 2-2zm0 4v13h10V5zm5 14.5a1.2 1.2 0 1 0 0 2.4 1.2 1.2 0 0 0 0-2.4z"/></svg>
        555 0198 3360
      </li>
      <li>
        <svg viewBox="0 0 24 24" aria-hidden="true"><path d="M2 5h20v14H2zm2 2v.5l8 5 8-5V7zm0 2.8V17h16V9.8l-8 5z"/></svg>
        sam@kmbuild.com
      </li>
    </ul>

    <div class="rule-address"></div>

    <div class="address">
      <div>412 Ochre Street</div>
      <div>Tennant Creek, NT 0860</div>
      <div class="address__web">www.kmbuild.com</div>
    </div>
  </section>
</body>
</html>
```